Brazilian wine business need a label for a sparkling wine

We are importing a new italian sparkling wine, but we need to build our own brand. Our main focus is to sell sparkling wine for events, specially for weddings. So, specially for this audience, presentation is key.
We like to see wine in a "uncomplicated" way.
It is a mid price product.
The foil capsule color must be black, white or silver, due to production restrictions. We cannot have any graphic interference in this part, also.

We need to develop a label for it. The name will be "Lumera Brut" (means "hug" in italian).

Our main public is people around the early 30s, so it should look modern and clean.
It is good, but not mandatory, to have a few information at the front label:
- Alcohol % (12%)
- Origin (Italy)

We need to avoid a few colours, for different reasons:
- Don´t use yellow/orange: too linked to Maison Dravelle;
- Don´t use red or pink: people think it is a rosé, but it is a white.
Our idea is to work with white and blue or turquoise, maybe a green, something like that. Can have a touch of gold, also. (more references in the color tab below)
- The bottle is black.

Industry/Entity Type

Business

Font styles to use
Other font styles liked:
• Berlin Sans FB Regular or something less "round" but similar to Cooper Black Regular

Colors
00a990
33b8a4

Requirements
Must have
• As the name means "hug", we want to have a graphic symbol that represents connections, alliances, symbiosis or infinite. I attached a few symbols that could be explore, but of course you can bring differente suggestions.
• We need a clean design, nothing with too many information.

```html
<!DOCTYPE html>
<html lang="pt">
<head>
<meta charset="utf-8">
<title>Lumera Brut – Rótulo</title>
<link rel="stylesheet" href="https://fonts.googleapis.com/css2?family=Josefin+Sans:wght@600&family=Oswald:wght@500&family=Roboto+Slab:wght@500&display=swap">
<style>
  :root {
    --backdrop: #0c0c0e;
    --label-navy: #1f3353;
    --label-navy-deep: #1b2d4a;
    --turquoise: #3fd0b8;
    --silver: #c7cfd8;
    --ornament-tone: #8e9aaa;
    --flag-green: #8cc63f;
    --flag-white: #f2f2f2;
    --flag-red: #e8403a;
  }
  html, body {
    margin: 0;
    width: 1200px;
    height: 1000px;
    overflow: hidden;
    background: var(--backdrop);
  }
  .label-art {
    display: block;
    width: 1200px;
    height: 1000px;
  }
  .arc-caption {
    font-family: "Josefin Sans", sans-serif;
    font-weight: 600;
    font-size: 28px;
    fill: var(--turquoise);
    letter-spacing: 3px;
  }
  .slab-text {
    font-family: "Roboto Slab", serif;
    font-weight: 500;
    fill: var(--turquoise);
  }
  .brand-name {
    font-family: "Oswald", sans-serif;
    font-weight: 500;
    fill: var(--turquoise);
    stroke: var(--silver);
    stroke-width: 2;
    paint-order: stroke;
  }
  .ornament { fill: var(--ornament-tone); opacity: .35; }
</style>
</head>
<body>
<svg class="label-art" viewBox="0 0 1200 1000" xmlns="http://www.w3.org/2000/svg">
  <defs>
    <path id="arc-top" d="M 310,470 A 290 290 0 0 1 890,470"/>
    <path id="arc-bottom" d="M 288,470 A 312 312 0 0 0 912,470"/>
    <clipPath id="inner-ring-clip">
      <rect x="0" y="0" width="1200" height="322"/>
      <rect x="0" y="600" width="1200" height="400"/>
    </clipPath>
  </defs>

  <!-- label body -->
  <g class="label-body">
    <ellipse cx="600" cy="470" rx="348" ry="358" fill="var(--label-navy)"/>
    <circle cx="600" cy="470" r="340" fill="none" stroke="var(--silver)" stroke-width="2"/>
    <circle cx="600" cy="470" r="334" fill="none" stroke="var(--turquoise)" stroke-width="5"/>
    <circle cx="600" cy="470" r="272" fill="var(--label-navy-deep)"/>
    <g class="inner-ring" clip-path="url(#inner-ring-clip)">
      <circle cx="600" cy="470" r="272" fill="none" stroke="var(--turquoise)" stroke-width="5"/>
      <circle cx="600" cy="470" r="278" fill="none" stroke="var(--silver)" stroke-width="1.5"/>
    </g>
  </g>

  <!-- arc captions -->
  <text class="arc-caption">
    <textPath href="#arc-top" startOffset="50%" text-anchor="middle">REGIÃO DE ORIGEM:</textPath>
  </text>
  <text class="arc-caption">
    <textPath href="#arc-bottom" startOffset="30%" text-anchor="middle">0.75 L</textPath>
  </text>
  <text class="arc-caption">
    <textPath href="#arc-bottom" startOffset="70%" text-anchor="middle">ALC. 12%</textPath>
  </text>

  <!-- ornament areas -->
  <rect class="ornament" x="344" y="276" width="40" height="12" rx="6" transform="rotate(-52 364 282)" role="img" aria-label="Ramo de folhas decorativo"/>
  <rect class="ornament" x="816" y="276" width="40" height="12" rx="6" transform="rotate(52 836 282)" role="img" aria-label="Ramo de folhas decorativo"/>
  <rect class="ornament" x="308" y="592" width="40" height="12" rx="6" transform="rotate(62 328 598)" role="img" aria-label="Ramo de folhas decorativo"/>
  <rect class="ornament" x="852" y="592" width="40" height="12" rx="6" transform="rotate(-62 872 598)" role="img" aria-label="Ramo de folhas decorativo"/>
  <rect class="ornament" x="562" y="776" width="76" height="12" rx="6" role="img" aria-label="Ramo de folhas decorativo"/>
  <rect class="ornament" x="448" y="252" width="44" height="32" rx="10" role="img" aria-label="Flor-de-lis decorativa"/>
  <rect class="ornament" x="708" y="252" width="44" height="32" rx="10" role="img" aria-label="Flor-de-lis decorativa"/>
  <rect class="ornament" x="428" y="620" width="40" height="40" rx="10" role="img" aria-label="Flor-de-lis decorativa"/>
  <rect class="ornament" x="732" y="620" width="40" height="40" rx="10" role="img" aria-label="Flor-de-lis decorativa"/>

  <!-- origin -->
  <text class="slab-text" x="600" y="286" font-size="62" text-anchor="middle">Itália</text>
  <g class="flag-bar">
    <rect x="537" y="306" width="43" height="8" fill="var(--flag-green)"/>
    <rect x="580" y="306" width="43" height="8" fill="var(--flag-white)"/>
    <rect x="623" y="306" width="44" height="8" fill="var(--flag-red)"/>
  </g>

  <!-- brand name -->
  <text class="brand-name" x="600" y="576" font-size="300" text-anchor="middle" textLength="560" lengthAdjust="spacingAndGlyphs">LUMERA</text>

  <!-- variety oval -->
  <g class="variety-badge">
    <ellipse cx="600" cy="662" rx="100" ry="62" fill="var(--label-navy-deep)" stroke="var(--silver)" stroke-width="2"/>
    <ellipse cx="600" cy="662" rx="94" ry="56" fill="none" stroke="var(--turquoise)" stroke-width="4"/>
    <circle cx="588" cy="622" r="3" fill="var(--silver)"/>
    <circle cx="600" cy="618" r="4" fill="var(--silver)"/>
    <circle cx="612" cy="622" r="3" fill="var(--silver)"/>
    <circle cx="588" cy="702" r="3" fill="var(--silver)"/>
    <circle cx="600" cy="706" r="4" fill="var(--silver)"/>
    <circle cx="612" cy="702" r="3" fill="var(--silver)"/>
    <text class="slab-text" x="600" y="684" font-size="60" text-anchor="middle">Brut</text>
  </g>
</svg>
</body>
</html>
```